Business school needs a web design

Who We are:
KRVT is a small business school that offers programs in Project Management. The school is based in West Africa and welcomes students from the whole area. Our aim is to become one of the reference business schools in Africa.

Project Brief:
The site will include all informations relevant for different types of visitors that we have: actual and future students, companies, mass media, future employees, ect. It will present information about subscription, list of programs, presentation of the school and its team,etc.

What We want:
This competition is for Design only no coding! We need design for two pages.
We did some wireframing for the home page and the list of programs page. We made them just to show how we imagine the website would look like. But we encourage creative designs, so you don't have to stick to the wireframe models.

Sites We like:
http://www.ravenmoorcollege.example/
http://www.belvantis.example/fr/etudes.html
http://www.qtl.example/mba/Pages/default.aspx

Color schemes
The logo of the school is red and black. So the color scheme of the website should match that. For the rest, it is opened to your imagination.
Updates

The payment for the project is now garanteed. Good luck to you all !

Target Market(s)

The target market is diversified because we have students of different ages, also company representatives or employees that might visit the website for recruitment purposes. But the majority of our audience should be aged between 20 - 30 years.

Industry/Entity Type

Small Business

Requirements
Must have
• The design must include two pages: a home page and another interior page : might be the list of programs or any other page relevant to the domain. The Home page must include a slide show at the beginning.
The background page must be white.
Nice to have
• The use of flat design for this project is preferred.
The use of Pelican scaffold as a base for the design is an asset.

```html
<!DOCTYPE html>
<html lang="fr">
<head>
<meta charset="utf-8">
<title>KRVT — Programmes et formations</title>
<link href="https://fonts.googleapis.com/css2?family=Roboto+Condensed:wght@400;700&family=Arimo:wght@400;700&display=swap" rel="stylesheet">
<style>
:root{
  --red:#d8403f;
  --red-soft:#d96c6a;
  --ink:#3c3c3c;
  --muted:#6e6e6e;
  --page:#ececec;
  --teal:#66c9b5;
  --teal-text:#4e8f82;
  --dark:#2f2f2f;
  --darker:#222;
  --white:#fff;
}
*{margin:0;padding:0;box-sizing:border-box}
html,body{width:905px;height:1200px;overflow:hidden}
body{background:var(--page);font-family:"Arimo",Arial,sans-serif;color:var(--ink);position:relative}
.abs{position:absolute}
.cond{font-family:"Roboto Condensed","Arial Narrow",sans-serif}

.topbar{top:0;left:0;width:905px;height:13px;background:var(--dark)}
.topbar .links{left:359px;top:1px;font-size:8px;color:#ddd;display:flex;gap:11px}
.search{left:630px;top:1px;width:94px;height:11px;background:#fff;font-size:6.5px;color:#888;padding:1px 3px}
.search-btn{left:710px;top:0;width:14px;height:13px;background:var(--red)}

.header{top:13px;left:0;width:905px;height:44px;background:#e8e8e8}
.brand{left:181px;top:27px;display:flex;align-items:center;gap:5px}
.brand .dot{width:10px;height:10px;background:var(--red)}
.brand span{font-family:"Roboto Condensed",sans-serif;font-weight:700;font-size:16px;color:var(--dark)}
.nav{top:30px;left:320px;width:404px;display:flex;justify-content:space-between;font-size:8.8px;font-weight:700;color:#444}
.nav .active{color:var(--ink);text-decoration:underline}

.hero{top:57px;left:0;width:905px;height:291px}
.hero-photo{top:0;left:0;width:905px;height:291px;background:linear-gradient(90deg,#6a5a55 0%,#b98a80 35%,#d5706c 60%,#d9605e 100%)}
.hero-strip{bottom:0;left:0;width:905px;height:23px;background:rgba(220,120,118,.85)}
.hero-box{left:408px;top:28px;width:277px;height:213px;background:rgba(175,70,68,.45);padding:0 9px}
.hero-box h2{font-family:"Roboto Condensed",sans-serif;font-weight:700;color:#fff;font-size:30px;margin-top:3px}
.hero-box p{color:#fff;font-size:7.6px;font-weight:700;line-height:11.3px;text-align:justify;margin-top:9px}
.arrow{top:120px}
.dots{left:436px;top:334px;display:flex;gap:4px}
.dots i{width:8px;height:8px;border-radius:50%;background:#eee}
.dots i.on{background:#999}

.crumb{left:181px;top:358px;font-size:8px}
.crumb a{color:var(--red);text-decoration:none}
.title{left:181px;top:378px;width:543px;font-family:"Roboto Condensed",sans-serif;font-weight:700;font-size:18.5px;color:#3a3a3a;border-bottom:1px solid #999;padding-bottom:1px}
.intro{left:181px;width:543px;font-size:10.2px;line-height:13.6px;color:var(--muted);text-align:justify}

.teal-band{top:644px;left:0;width:905px;height:180px;background:var(--teal)}
.col{width:170px}
.col h3{font-family:"Roboto Condensed",sans-serif;font-weight:700;font-size:13px;color:#444}
.video{margin-top:12px;width:170px;height:113px;background:linear-gradient(135deg,#5b5250,#8a7a72 60%,#3f3a38);position:relative;box-shadow:0 1px 3px rgba(0,0,0,.3)}
.video .play{position:absolute;left:61px;top:36px;width:48px;height:32px;border-radius:5px;background:rgba(20,20,20,.8)}
.video .bar{position:absolute;left:0;bottom:0;width:170px;height:10px;background:#e5e5e5}
.col h4{margin-top:10px;font-family:"Roboto Condensed",sans-serif;font-size:10px;color:var(--teal-text);font-weight:700}
.col p{margin-top:11px;font-size:7.3px;line-height:11.3px;color:var(--teal-text);text-align:justify}

.sub-title{left:181px;top:832px;width:543px;font-family:"Roboto Condensed",sans-serif;font-weight:700;font-size:12.5px;color:#3a3a3a;border-bottom:1px solid #999;padding-bottom:1px}
.program{width:265px;display:flex;gap:8px}
.program .book{flex:none;width:54px;height:54px}
.program h5{font-family:"Roboto Condensed",sans-serif;font-weight:700;font-size:10px;color:#444}
.program p{font-size:7.3px;line-height:10.2px;color:var(--muted);margin-top:4px;text-align:justify}

.footer{top:1048px;left:0;width:905px;height:138px;background:var(--dark)}
.fcol h6{font-family:"Roboto Condensed",sans-serif;font-weight:700;font-size:13px;color:#fff;border-bottom:1px solid #ccc;padding-bottom:2px;width:100px}
.fcol ul{list-style:none;margin-top:14px}
.fcol li{font-size:7.8px;font-weight:700;color:#fff;line-height:14.5px}
.addr h6{color:var(--red);border:none}
.addr b{display:block;margin-top:14px;font-size:9.3px;color:#fff}
.addr small{display:block;font-size:7.6px;font-weight:700;color:#fff;line-height:11px;width:130px}
.phone{display:flex;align-items:center;gap:9px;font-size:10px;font-weight:700;color:#fff;margin-top:6px}
.vsep{left:599px;top:1094px;width:1px;height:72px;background:#ccc}
.follow{left:622px;top:1056px;width:102px;text-align:right;font-family:"Roboto Condensed",sans-serif;font-weight:700;font-size:13px;color:var(--teal);border-bottom:1px solid #ccc;padding-bottom:2px}
.socials{left:622px;top:1113px;display:flex;gap:4px}
.socials i{width:22px;height:25px;display:block}
.legal{top:1186px;left:0;width:905px;height:14px;background:var(--darker);text-align:center;font-size:7px;font-weight:700;color:#eee;line-height:14px}
</style>
</head>
<body>

<div class="abs topbar">
  <div class="abs links"><span>Répertoire du personnel</span><span>Blog</span><span>Salle de presse</span><span>Contact</span></div>
  <div class="abs search">Recherche</div>
  <div class="abs search-btn"></div>
</div>

<div class="abs header"></div>
<div class="abs brand"><div class="dot"></div><span>KRVT</span></div>
<nav class="abs nav"><span>KRVT</span><span class="active">Programmes et formations</span><span>Etudiants</span><span>Nouvelles et évènements</span><span>Entreprises</span></nav>

<section class="abs hero">
  <div class="abs hero-photo" role="img" aria-label="Photo d'un amphithéâtre avec un enseignant face aux étudiants, teintée de rouge"></div>
  <div class="abs hero-strip"></div>
  <svg class="abs arrow" style="left:180px" width="26" height="34" viewBox="0 0 26 34"><path d="M22 2 5 17l17 15" fill="none" stroke="#fff" stroke-opacity=".7" stroke-width="3"/></svg>
  <svg class="abs arrow" style="left:698px" width="26" height="34" viewBox="0 0 26 34"><path d="M4 2l17 15L4 32" fill="none" stroke="#fff" stroke-opacity=".85" stroke-width="3"/></svg>
  <div class="abs hero-box">
    <h2>KRVT</h2>
    <p>Lorem ipsum dolor sit amet, consectetur adipiscing elit. Phasellus venenatis pellentesque aliquet. Fusce auctor est ut dolor dignissim, non tempor leo ornare. Sed eget tristique libero. Aliquam dapibus est ac eros consectetur, molestie placerat justo eleifend.</p>
    <p>Lorem ipsum dolor sit amet, consectetur adipiscing elit. Phasellus venenatis pellentesque aliquet. Fusce auctor est ut dolor dignissim, non tempor leo ornare. Sed eget tristique libero. Aliquam dapibus est ac eros consectetur, molestie placerat justo eleifend.</p>
    <p>Fusce auctor est ut dolor dignissim, non tempor leo ornare. Sed eget tristique libero. Aliquam dapibus est ac eros consectetur, molestie placerat justo eleifend.</p>
  </div>
</section>
<div class="abs dots"><i></i><i class="on"></i><i></i></div>

<div class="abs crumb"><a href="#">Accueil</a> &nbsp;/&nbsp; Programmes et formations</div>
<h1 class="abs title">PROGRAMMES ET FORMATIONS</h1>
<p class="abs intro" style="top:415px">Etiam tortor leo, euismod quis est in, convallis bibendum ante. Ut consequat justo mi, eget bibendum orci consectetur tincidunt. Fusce id nunc interdum, accumsan elit in, porttitor erat. Proin non vestibulum erat, in placerat nibh. Pellentesque fringilla mi laoreet, mollis metus sit amet, rhoncus felis.</p>
<p class="abs intro" style="top:469px">Duis euismod odio ante, nec interdum magna semper sit amet. Cras vel turpis consequat, mattis sem pharetra, tempus purus. Duis sagittis vulputate turpis id vestibulum. Quisque sed elit sem. Vestibulum luctus, risus sit amet feugiat elementum, ante dui auctor quam,</p>

<div class="abs teal-band"></div>

<div class="abs col" style="left:181px;top:555px">
  <h3>Formations diplomantes</h3>
  <div class="video" role="img" aria-label="Vidéo : étudiants en cours"><div class="play"></div><div class="bar"></div>
    <svg style="position:absolute;left:80px;top:46px" width="12" height="12"><path d="M1 0l10 6-10 6z" fill="#fff"/></svg></div>
  <h4>Lorem ipsum</h4>
  <p>Duis euismod odio ante, nec interdum magna semper sit amet. Cras vel turpis consequat, mattis sem pharetra, tempus purus. Duis sagittis vulputate turpis id vestibulum. Quisque sed elit sem. Vestibulum luctus, risus sit amet feugiat elementum, ante dui auctor quam,</p>
</div>
<div class="abs col" style="left:367px;top:555px">
  <h3>Certificats professionnels</h3>
  <div class="video" role="img" aria-label="Vidéo : travail en groupe"><div class="play"></div><div class="bar"></div>
    <svg style="position:absolute;left:80px;top:46px" width="12" height="12"><path d="M1 0l10 6-10 6z" fill="#fff"/></svg></div>
  <h4>Lorem ipsum</h4>
  <p>Duis euismod odio ante, nec interdum magna semper sit amet. Cras vel turpis consequat, mattis sem pharetra, tempus purus. Duis sagittis vulputate turpis id vestibulum. Quisque sed elit sem. Vestibulum luctus, risus sit amet feugiat elementum, ante dui auctor quam,</p>
</div>
<div class="abs col" style="left:553px;top:555px">
  <h3>Formations à la carte</h3>
  <div class="video" role="img" aria-label="Vidéo : enseignant au tableau"><div class="play"></div><div class="bar"></div>
    <svg style="position:absolute;left:80px;top:46px" width="12" height="12"><path d="M1 0l10 6-10 6z" fill="#fff"/></svg></div>
  <h4>Lorem ipsum</h4>
  <p>Duis euismod odio ante, nec interdum magna semper sit amet. Cras vel turpis consequat, mattis sem pharetra, tempus purus. Duis sagittis vulputate turpis id vestibulum. Quisque sed elit sem. Vestibulum luctus, risus sit amet feugiat elementum, ante dui auctor quam,</p>
</div>

<h2 class="abs sub-title">PROGRAMMES OFFERTS</h2>

<svg width="0" height="0" style="position:absolute">
  <symbol id="book" viewBox="0 0 54 54">
    <rect x="6" y="4" width="40" height="44" rx="2" fill="#d8403f"/>
    <rect x="14" y="9" width="27" height="34" fill="none" stroke="#fff" stroke-width="1.5"/>
    <path d="M20 10v32M27 10v32M34 10v32" stroke="#f4b0ae" stroke-width="2"/>
    <g fill="#fff"><circle cx="6" cy="10" r="2"/><circle cx="6" cy="18" r="2"/><circle cx="6" cy="26" r="2"/><circle cx="6" cy="34" r="2"/><circle cx="6" cy="42" r="2"/></g>
    <path d="M0 50h54" stroke="#d8403f" stroke-width="2"/>
  </symbol>
</svg>

<div class="abs program" style="left:181px;top:882px"><svg class="book"><use href="#book"/></svg><div><h5>Lorem ipsum</h5><p>Praesent tempor non sapien sed placerat. Nullam a mi posuere metus varius suscipit. Etiam libero erat, convallis eget arcu nec, pellentesque pretium nulla. Mauris vestibulum purus nec mi.</p></div></div>
<div class="abs program" style="left:459px;top:882px"><svg class="book"><use href="#book"/></svg><div><h5>Lorem ipsum</h5><p>Praesent tempor non sapien sed placerat. Nullam a mi posuere metus varius suscipit. Etiam libero erat, convallis eget arcu nec, pellentesque pretium nulla. Mauris vestibulum purus nec mi.</p></div></div>
<div class="abs program" style="left:181px;top:962px"><svg class="book"><use href="#book"/></svg><div><h5>Lorem ipsum</h5><p>Praesent tempor non sapien sed placerat. Nullam a mi posuere metus varius suscipit. Etiam libero erat, convallis eget arcu nec, pellentesque pretium nulla. Mauris vestibulum purus nec mi.</p></div></div>
<div class="abs program" style="left:459px;top:962px"><svg class="book"><use href="#book"/></svg><div><h5>Lorem ipsum</h5><p>Praesent tempor non sapien sed placerat. Nullam a mi posuere metus varius suscipit. Etiam libero erat, convallis eget arcu nec, pellentesque pretium nulla. Mauris vestibulum purus nec mi.</p></div></div>

<footer class="abs footer"></footer>
<div class="abs fcol" style="left:181px;top:1056px"><h6>A PROPOS</h6><ul><li>KRVT</li><li>Admissions</li><li>Calendrier de l'école</li><li>Offres d'emplois</li><li>Répertoire du personnel</li></ul></div>
<div class="abs fcol" style="left:322px;top:1056px"><h6>ETUDIANTS</h6><ul><li>Accueil - Etudiants</li><li>Programmes et formations</li><li>Vie étudiante</li><li>Entreprises</li><li>Blog</li></ul></div>
<div class="abs fcol addr" style="left:458px;top:1056px"><h6>KRVT</h6>
  <b>14, AVENUE DES BAOBABS</b><small>Près du carrefour du vieux marché central</small>
  <div class="phone" style="margin-top:10px"><svg width="12" height="12" viewBox="0 0 24 24"><path d="M6.6 10.8a15 15 0 0 0 6.6 6.6l2.2-2.2c.3-.3.7-.4 1-.2 1.1.4 2.3.6 3.6.6.6 0 1 .4 1 1V20c0 .6-.4 1-1 1A17 17 0 0 1 3 4c0-.6.4-1 1-1h3.5c.6 0 1 .4 1 1 0 1.3.2 2.5.6 3.6.1.3 0 .7-.2 1z" fill="#fff"/></svg>( 000 ) 11 240 60 71</div>
  <div class="phone"><svg width="12" height="12" viewBox="0 0 24 24"><path d="M6.6 10.8a15 15 0 0 0 6.6 6.6l2.2-2.2c.3-.3.7-.4 1-.2 1.1.4 2.3.6 3.6.6.6 0 1 .4 1 1V20c0 .6-.4 1-1 1A17 17 0 0 1 3 4c0-.6.4-1 1-1h3.5c.6 0 1 .4 1 1 0 1.3.2 2.5.6 3.6.1.3 0 .7-.2 1z" fill="#fff"/></svg>( 000 ) 11 240 60 71</div>
</div>
<div class="abs vsep"></div>
<div class="abs follow">SUIVEZ-NOUS</div>
<div class="abs socials">
  <i style="background:#3b5a9a" aria-label="Réseau social 1"></i>
  <i style="background:#2e9bd6" aria-label="Réseau social 2"></i>
  <i style="background:#d8403f" aria-label="Réseau social 3"></i>
  <i style="background:#2b7aa8" aria-label="Réseau social 4"></i>
</div>
<div class="abs legal">Tous droits réservés @ Studio Nalo 2014</div>

</body>
</html>
```